Pellow Studio Website Design

Home page & interior page design.

Target Market(s)

Small businesses or at home businesses. Budget $1,000 - $3,000.

Industry/Entity Type

Media

Number of Pages Required

2 pages

Requirements
Must have
• Home page must consist of:
- Logo in top left
- Bannerimagery showcasing design examples (to be provided)
- 4 main modules, directing users to the 4 main product areas:
1. Templated brochure websites
2. Custom designed brochure websites
3. eCommerce websites
4. SEO

Area for text to be inserted (around 200 words) of introductory text

- Use of correct colour pallette based on logo provided
Nice to have
• Custom designed icons for the 4 main product areas.
Should not have
• Unstructured, cluttered layout

```html
<!DOCTYPE html>
<html lang="en">
<head>
<meta charset="utf-8">
<title>Pellow Studio – Home</title>
<link href="https://fonts.googleapis.com/css2?family=Yanone+Kaffeesatz:wght@500;600&family=Noto+Sans:wght@400&display=swap" rel="stylesheet">
<style>
  :root {
    --backdrop: #3d3d3d;
    --page: #ffffff;
    --band: #e8e8e8;
    --heading-red: #e41e1e;
    --brand-orange: #f0861c;
    --orange-light: #fbb33a;
    --orange-deep: #f27417;
    --marker-light: #fcd23c;
    --marker-deep: #f29418;
    --text: #1f1f1f;
  }
  * { box-sizing: border-box; margin: 0; padding: 0; }
  html, body {
    width: 1200px; height: 900px; overflow: hidden;
    background: var(--backdrop);
  }
  .page {
    position: absolute; left: 137px; top: 53px;
    width: 933px; height: 797px;
    background: var(--page);
    font-family: "Noto Sans", Verdana, sans-serif;
    color: var(--text);
  }
  .brand {
    position: absolute; left: 39px; top: 48px;
    font-family: "Yanone Kaffeesatz", sans-serif;
    font-weight: 600; font-size: 50px; line-height: 1;
    color: var(--brand-orange);
  }
  .showcase { position: absolute; }
  .showcase--dark {
    left: 375px; top: 3px; width: 147px; height: 126px;
    background: linear-gradient(180deg, #101a33 0%, #1f3560 45%, #e38a2a 62%, #26324f 80%, rgba(40,50,80,0.2) 100%);
  }
  .showcase--blue {
    left: 564px; top: 6px; width: 158px; height: 150px;
    background: linear-gradient(180deg, #ffffff 0%, #2a9ad6 12%, #55b7e6 45%, #f4f6f8 55%, rgba(240,242,245,0.3) 100%);
  }
  .showcase--sunset {
    left: 763px; top: 8px; width: 156px; height: 162px;
    background: linear-gradient(180deg, #222 0%, #d9772b 12%, #f2a14a 30%, #efefef 45%, rgba(240,240,240,0.25) 100%);
  }
  .module { position: absolute; left: 0; width: 933px; }
  .module--white { background: var(--page); }
  .module--grey { background: var(--band); }
  .module--templates { top: 0; height: 296px; }
  .module--custom { top: 296px; height: 164px; }
  .module--commerce { top: 460px; height: 153px; }
  .module--search { top: 613px; height: 164px; }

  .module__title {
    position: absolute;
    display: flex; align-items: flex-start; gap: 6px;
    font-family: "Yanone Kaffeesatz", sans-serif;
    font-weight: 600; font-size: 47px; line-height: 1;
    color: var(--heading-red);
    white-space: nowrap;
  }
  .module__title--left { left: 164px; }
  .module__title--right { right: 161px; flex-direction: row-reverse; }
  .marker {
    display: block; width: 22px; height: 44px; flex: none; margin-top: -4px;
    border-radius: 3px;
    background: linear-gradient(180deg, var(--marker-light), var(--marker-deep));
  }

  .module__text {
    position: absolute; width: 790px;
    font-size: 13.4px; line-height: 18.7px;
    white-space: nowrap;
  }
  .module__text--left { left: 166px; }
  .module__text--right { left: 9px; }

  .module__icon {
    position: absolute; width: 146px; height: 146px;
    border-radius: 50%;
    background: radial-gradient(circle at 50% 35%, var(--orange-light) 0%, var(--orange-deep) 75%);
    border: 3px solid #fde6c2;
    box-shadow: 0 2px 8px rgba(120,60,0,0.55);
    display: flex; align-items: center; justify-content: center;
  }
  .search-label {
    display: flex; flex-direction: column; align-items: center;
    color: #fff; font-family: "Noto Sans", sans-serif; font-size: 31px; line-height: 1;
  }
  .search-label span { display: block; width: 108px; height: 12px; background: #fff; margin-top: 8px; }

  .footer {
    position: absolute; left: 0; top: 777px; width: 933px; height: 20px;
    text-align: center; font-size: 13px; line-height: 20px;
  }
</style>
</head>
<body>
<main class="page">
  <div class="module module--white module--templates">
    <div class="brand">Pellow Studio</div>
    <div class="showcase showcase--dark" role="img" aria-label="Dark website design example"></div>
    <div class="showcase showcase--blue" role="img" aria-label="Blue website design example"></div>
    <div class="showcase showcase--sunset" role="img" aria-label="Business website design example with sunset banner"></div>

    <div class="module__icon" style="left:4px; top:149px;" role="img" aria-label="Templates icon badge"></div>
    <h2 class="module__title module__title--left" style="top:157px;">Templates<span class="marker" role="img" aria-label="Heading marker"></span></h2>
    <p class="module__text module__text--left" style="top:202px;">Lorem ipsum dolor sit amet, consectetur adipiscing elit. Curabitur arcu tellus, commodo vitae euismod ullamcorper,<br>euismod ac eros. Maecenas nisi ipsum, bibendum ut rutrum vel, faucibus sit amet mi. Etiam eros lectus, varius sed<br>aliquam in, consectetur ac nunc. Curabitur eget nunc diam. Suspendisse potenti. Nulla consectetur pulvinar nisl eget<br>volutpat. Suspendisse convallis ultrices libero, ut vulputate sapien eleifend elementum.</p>
  </div>

  <div class="module module--grey module--custom">
    <h2 class="module__title module__title--right" style="top:10px;">Custom Design<span class="marker" role="img" aria-label="Heading marker"></span></h2>
    <p class="module__text module__text--right" style="top:52px;">Lorem ipsum dolor sit amet, consectetur adipiscing elit. Curabitur arcu tellus, commodo vitae euismod ullamcorper,<br>euismod ac eros. Maecenas nisi ipsum, bibendum ut rutrum vel, faucibus sit amet mi. Etiam eros lectus, varius sed<br>aliquam in, consectetur ac nunc. Curabitur eget nunc diam. Suspendisse potenti. Nulla consectetur pulvinar nisl eget<br>volutpat. Suspendisse convallis ultrices libero, ut vulputate sapien eleifend elementum.</p>
    <div class="module__icon" style="left:774px; top:7px;" role="img" aria-label="Custom design icon badge"></div>
  </div>

  <div class="module module--white module--commerce">
    <div class="module__icon" style="left:3px; top:6px;" role="img" aria-label="E-commerce icon badge"></div>
    <h2 class="module__title module__title--left" style="top:-4px;">E-Commerce<span class="marker" role="img" aria-label="Heading marker"></span></h2>
    <p class="module__text module__text--left" style="top:40px;">Lorem ipsum dolor sit amet, consectetur adipiscing elit. Curabitur arcu tellus, commodo vitae euismod ullamcorper,<br>euismod ac eros. Maecenas nisi ipsum, bibendum ut rutrum vel, faucibus sit amet mi. Etiam eros lectus, varius sed<br>aliquam in, consectetur ac nunc. Curabitur eget nunc diam. Suspendisse potenti. Nulla consectetur pulvinar nisl eget<br>volutpat. Suspendisse convallis ultrices libero, ut vulputate sapien eleifend elementum.</p>
  </div>

  <div class="module module--grey module--search">
    <h2 class="module__title module__title--right" style="top:2px;">Search Optimisation<span class="marker" role="img" aria-label="Heading marker"></span></h2>
    <p class="module__text module__text--right" style="top:56px; left:10px;">Lorem ipsum dolor sit amet, consectetur adipiscing elit. Curabitur arcu tellus, commodo vitae euismod ullamcorper,<br>euismod ac eros. Maecenas nisi ipsum, bibendum ut rutrum vel, faucibus sit amet mi. Etiam eros lectus, varius sed<br>aliquam in, consectetur ac nunc. Curabitur eget nunc diam. Suspendisse potenti. Nulla consectetur pulvinar nisl eget<br>volutpat. Suspendisse convallis ultrices libero, ut vulputate sapien eleifend elementum.</p>
    <div class="module__icon" style="left:774px; top:5px;">
      <div class="search-label">Search<span></span></div>
    </div>
  </div>

  <footer class="footer">Copyright PellowStudio 2009 | Disclaimer | Last Updated 11/09/09</footer>
</main>
</body>
</html>
```